依頼概要
第33回白鷺川大星火大会
2018年7月14日(土)午後7時30分開会
関東最大級22800発
三大花火師夢の饗宴 桐原煙火工業・宮田火工製作所・藤屋松井火工店
主催:北浜町観光協会・きたはまみなと祭り実行委員会
後援:北浜町・北浜町議会・七森町・北浜町商工会・七森町商工会・JA北陸あおば
問い合わせ:北浜町観光協会 TEL0280-81-1319
北浜町で検索的なもの
観覧チケットの購入はチケミナで検索的なもの

若干の構成を再度お願いする場合もあります。また、制作いただきました作品に、場合によりこちらで後援や開催日時等軽微な修正をする場合があります。
http://filevault-sample.jp/photo/3c1a9e07b42d58f6a0e9c2147bd86f03e5a1c9d2
上記URLは添付にあるものと同様の使用する写真です

町長様・観光協会様の方で候補作品から選んでいただきました。

ご参加・ご協力ありがとうございました。

```html
<!DOCTYPE html>
<html lang="ja">
<head>
<meta charset="utf-8">
<title>第33回白鷺川大星火大会</title>
<link href="https://fonts.googleapis.com/css2?family=Yuji+Boku&family=Noto+Serif+JP:wght@700;900&family=Noto+Sans+JP:wght@400;700&display=swap" rel="stylesheet">
<style>
:root{
  --night:#05050a;
  --white:#ffffff;
  --gold:#ffd84a;
  --red:#e0102a;
  --pink:#ff3d6e;
  --ink:#1a1a1a;
  --grey:#555;
}
*{margin:0;padding:0;box-sizing:border-box}
html,body{width:849px;height:1200px;overflow:hidden;background:var(--night)}
.poster{position:relative;width:849px;height:1200px;background:var(--night);overflow:hidden;font-family:"Noto Sans JP",sans-serif;color:var(--white)}
.fireworks-photo{position:absolute;left:0;top:0;width:849px;height:990px;
  background:
    radial-gradient(ellipse 240px 200px at 200px 190px,rgba(255,220,140,.55),transparent 70%),
    radial-gradient(ellipse 260px 220px at 560px 170px,rgba(255,240,190,.6),transparent 70%),
    radial-gradient(ellipse 200px 160px at 760px 300px,rgba(255,90,140,.45),transparent 70%),
    radial-gradient(ellipse 180px 160px at 90px 400px,rgba(255,120,170,.4),transparent 70%),
    linear-gradient(180deg,#15121a 0%,#2a1c14 40%,#6a4a20 58%,#0a0808 78%,#05050a 100%);}
.badge{position:absolute;left:50px;top:578px;width:90px;height:90px;border-radius:50%;background:var(--red);border:3px solid var(--gold);
  display:flex;align-items:center;justify-content:center;white-space:nowrap;font-family:"Noto Serif JP",serif;font-weight:900;font-size:17px;color:var(--gold)}
.badge b{font-size:30px;line-height:1}
.headline{position:absolute;left:158px;top:590px;white-space:nowrap;font-family:"Noto Serif JP",serif;font-weight:900;font-size:46px;line-height:1.3;color:var(--gold);letter-spacing:2px;text-shadow:0 0 6px #000}
.title{position:absolute;left:0;width:849px;top:668px;text-align:center;white-space:nowrap;font-family:"Yuji Boku",serif;font-weight:400;font-size:82px;line-height:1.2;color:var(--white);
  text-shadow:3px 3px 0 var(--red),-2px -2px 0 var(--pink),0 0 12px var(--red)}
.title .big{font-size:108px}
.date{position:absolute;left:0;width:849px;top:808px;text-align:center;white-space:nowrap;font-family:"Noto Serif JP",serif;font-weight:700;font-size:24px;line-height:1.4;color:var(--white)}
.date em{font-style:normal;color:var(--gold);font-size:30px}
.tagline{position:absolute;left:0;width:849px;top:852px;text-align:center;white-space:nowrap;font-family:"Noto Serif JP",serif;font-weight:900;font-size:42px;line-height:1.3;letter-spacing:4px}
.makers{position:absolute;left:0;width:849px;top:918px;text-align:center;white-space:nowrap;font-family:"Noto Serif JP",serif;font-weight:900;font-size:29px;line-height:1.3}
.makers .sep{color:var(--gold);margin:0 8px}
.info-band{position:absolute;left:0;top:990px;width:849px;height:210px;background:var(--white);color:var(--ink);padding:26px 30px 0}
.info-row{display:flex;justify-content:space-between;align-items:flex-start}
.search-list{font-size:15px;line-height:2.2}
.search-line{display:flex;align-items:center;gap:10px;white-space:nowrap}
.search-box{display:inline-flex;border:1.5px solid var(--ink);height:26px;align-items:center}
.search-box span{padding:0 10px;font-weight:700;font-size:15px;min-width:130px}
.search-box i{font-style:normal;background:var(--ink);color:var(--white);padding:0 10px;height:100%;display:flex;align-items:center;font-size:13px}
.contact{text-align:right;font-size:15px;line-height:1.7;white-space:nowrap}
.contact strong{font-size:26px;color:var(--red)}
.sponsors{position:absolute;left:0;bottom:0;width:849px;padding:12px 20px;font-size:12.5px;white-space:nowrap;color:var(--grey);line-height:1.6;border-top:1px solid #ccc}
</style>
</head>
<body>
<div class="poster">
  <div class="fireworks-photo" role="img" aria-label="夜空に広がる大輪の打ち上げ花火と水面近くのスターマイン"></div>

  <div class="badge"><span>第<b>33</b>回</span></div>
  <div class="headline">関東最大級 2万2800発</div>
  <h1 class="title">白鷺川<span class="big">大星火</span>大会</h1>
  <p class="date">2018年<em>7</em>月<em>14</em>日(土) 午後<em>7</em>時<em>30</em>分 開会</p>
  <p class="tagline">三代花火師 夢の饗宴</p>
  <p class="makers">桐原煙火工業<span class="sep">/</span>宮田火工製作所<span class="sep">/</span>藤屋松井火工店</p>

  <section class="info-band">
    <div class="info-row">
      <div class="search-list">
        <div class="search-line">観覧チケットの購入はこちら <span class="search-box"><span>チケミナ</span><i>検索</i></span></div>
        <div class="search-line">最新情報はこちらから確認 <span class="search-box"><span>北浜町</span><i>検索</i></span></div>
      </div>
      <div class="contact">お問い合わせ 北浜町観光協会<br><strong>TEL 0290-64-7725</strong></div>
    </div>
    <p class="sponsors">【主催】北浜町観光協会・きたはまみなと祭り実行委員会 【後援】北浜町・北浜町議会・七森町・北浜町商工会・七森町商工会・JA北陸あおば</p>
  </section>
</div>
</body>
</html>
```